Global Leadership Company requires banner design

I need 3 large banners designed. i will be using these for advertising and also a condensed version as the header on a splash pages.

I have attached the wording and also the photo's that i'd like used in each design.
Note: i've just placed the wording randomly, you'll have to place it where it makes the most sense for the message and the design.

I want something with bright colors that pops.

Reason: I'd like to give the most recent designers time to submit quality work.

```html
<!DOCTYPE html>
<html lang="en">
<head>
<meta charset="utf-8">
<title>Leadership Opportunity Banners</title>
<link href="https://fonts.googleapis.com/css2?family=Sora:wght@300;400;500;600;700&display=swap" rel="stylesheet">
<style>
:root{
  --red:#ed1c24;
  --red-dark:#a3161c;
  --bubble:#c8141b;
  --green:#0d9b3a;
  --green-text:#1aa33c;
  --ink:#111111;
  --white:#ffffff;
  --ribbon:#1c1c1c;
  --bg-dark:#6d6e71;
  --bg-light:#d4d5d7;
}
*{margin:0;padding:0;box-sizing:border-box}
html,body{width:1200px;height:1000px;overflow:hidden}
body{
  font-family:"Sora",Arial,sans-serif;
  background:linear-gradient(135deg,var(--bg-dark) 0%,#a7a8aa 45%,var(--bg-light) 100%);
  position:relative;
}
.banner{position:absolute;left:160px;width:880px;height:263px;overflow:hidden}
.abs{position:absolute}
.photo{position:absolute}

/* Banner 1 */
.banner-wanted{top:65px;background:linear-gradient(160deg,#ffffff 0%,#f1f1f1 40%,#ffffff 60%,#e9e9e9 100%)}
.wanted-title{left:27px;top:8px;font-size:63px;font-weight:600;color:var(--red);letter-spacing:-1px}
.wanted-sub{left:28px;top:82px;font-size:18.5px;font-weight:300;color:var(--red-dark);line-height:23px;width:320px}
.ribbon{left:25px;top:146px;width:315px;height:39px}
.ribbon-text{left:25px;top:146px;width:315px;height:39px;line-height:39px;text-align:center;color:var(--white);font-size:19px;font-weight:500}
.boom{left:27px;top:196px;font-size:19px;font-weight:500;color:var(--ink)}
.wanted-quote{left:376px;top:20px;width:330px;font-size:17.5px;font-weight:500;line-height:23px;color:var(--ink)}
.perk-list{left:376px;top:96px;list-style:none;font-size:13.5px;color:var(--green-text);font-weight:500}
.perk-list li{height:26px}
.photo-woman{left:731px;top:0;width:149px;height:227px;background:linear-gradient(180deg,#6b5b47 0%,#b89a76 45%,#d7b08c 70%,#8a7462 100%)}
.bubble{left:575px;top:110px;width:180px;height:110px}
.bubble-text{left:582px;top:127px;width:160px;text-align:center;font-size:11px;line-height:16px;color:var(--white);white-space:nowrap}
.bubble-text b{font-weight:600}
.wanted-bar{left:0;top:227px;width:880px;height:36px}
.bar-left-text{left:60px;top:227px;line-height:36px;font-size:19px;font-weight:500;color:var(--white)}
.bar-right-text{left:522px;top:227px;line-height:36px;font-size:19px;font-weight:500;color:var(--red-dark)}

/* Banner 2 */
.banner-develop{top:371px;background:linear-gradient(160deg,#fbe0e0 0%,#ffffff 35%,#f6c9cc 60%,#fde8e8 100%)}
.photo-couple-formal{left:0;top:0;width:167px;height:159px;background:linear-gradient(160deg,#2a2424 0%,#4a3a33 40%,#6e5846 70%,#1c1818 100%)}
.tab{left:0;top:0;width:880px;height:31px}
.tab-text{left:550px;top:0;line-height:31px;font-size:18.5px;font-weight:500;color:var(--white)}
.question-list{left:192px;top:50px;list-style:none;font-size:18px;font-weight:500;color:var(--ink)}
.question-list li{height:32px}
.develop-band{left:0;top:159px;width:880px;height:67px;background:var(--red);color:var(--white);text-align:center;font-size:19.5px;font-weight:500;line-height:26px;padding-top:8px}
.develop-strip{left:0;top:233px;width:880px;height:30px;background:var(--green);display:flex;justify-content:space-between;align-items:center;padding:0 20px 0 22px;color:var(--white);font-size:13.5px;font-weight:500}

/* Banner 3 */
.banner-tomorrow{top:671px;background:linear-gradient(180deg,var(--red) 0%,var(--red) 60%,#c4151c 100%)}
.tab-light-text{left:550px;top:0;line-height:31px;font-size:18.5px;font-weight:500;color:var(--green-text)}
.tomorrow-title{left:45px;top:48px;font-size:41px;font-weight:500;color:var(--white);letter-spacing:.3px}
.tomorrow-lines{left:45px;top:111px;font-size:17.5px;font-weight:500;color:var(--ink);line-height:28px}
.tomorrow-note{left:104px;top:188px;font-size:13.5px;color:var(--white)}
.photo-couple-casual{left:678px;top:101px;width:202px;height:133px;background:linear-gradient(160deg,#141010 0%,#3c2c24 45%,#6a5242 65%,#120e0c 100%)}
.tomorrow-strip{left:0;top:234px;width:880px;height:29px;background:var(--white);display:flex;justify-content:space-between;align-items:center;padding:0 62px 0 53px;color:var(--green-text);font-size:13.5px;font-weight:500}
</style>
</head>
<body>

<section class="banner banner-wanted">
  <h1 class="abs wanted-title">WANTED!</h1>
  <p class="abs wanted-sub">Driven Individuals READY to take their results to the next level...</p>
  <svg class="abs ribbon" viewBox="0 0 315 39" aria-hidden="true">
    <polygon points="0,0 315,0 308,19.5 315,39 0,39 7,19.5" fill="var(--ribbon)"/>
    <rect x="9" y="0" width="297" height="39" fill="#262626"/>
  </svg>
  <p class="abs ribbon-text">PERSONAL EMPOWERMENT</p>
  <p class="abs boom">...the NEXT Big Business Boom!</p>
  <p class="abs wanted-quote">“Let us show you how we’ve taught average people to earn executive salary from home - part time. FAST!”</p>
  <ul class="abs perk-list">
    <li>- Make us to $5,000 per sale</li>
    <li>- No cold calling</li>
    <li>- No experience required</li>
    <li>- No pressure selling</li>
    <li>- NOT MLM</li>
  </ul>
  <div class="photo photo-woman" role="img" aria-label="Portrait photo of a smiling blonde woman"></div>
  <svg class="abs bubble" viewBox="0 0 180 110" aria-hidden="true">
    <polygon points="126,22 170,2 158,52" fill="var(--bubble)"/>
    <ellipse cx="87" cy="55" rx="83" ry="47" fill="var(--bubble)"/>
  </svg>
  <p class="abs bubble-text">“Within just 5<br>months I was making<br>over $25,000 per month”<br><b>- Dana, Colorado</b></p>
  <svg class="abs wanted-bar" viewBox="0 0 880 36" aria-hidden="true">
    <defs>
      <linearGradient id="barRed" x1="0" y1="0" x2="0" y2="1">
        <stop offset="0" stop-color="#ed1c24"/><stop offset="1" stop-color="#b5161c"/>
      </linearGradient>
    </defs>
    <rect width="880" height="36" fill="#ffffff"/>
    <polygon points="0,0 520,0 488,36 0,36" fill="url(#barRed)"/>
  </svg>
  <p class="abs bar-left-text">JUST LAUNCHED IN THE UNITED STATES</p>
  <p class="abs bar-right-text">CLICK HERE FOR FREE INFO ➜</p>
</section>

<section class="banner banner-develop">
  <div class="photo photo-couple-formal" role="img" aria-label="Photo of a man in a tuxedo and a blonde woman at an evening event"></div>
  <svg class="abs tab" viewBox="0 0 880 31" aria-hidden="true">
    <defs>
      <linearGradient id="tabRed" x1="0" y1="0" x2="0" y2="1">
        <stop offset="0" stop-color="#ed1c24"/><stop offset="1" stop-color="#9e1318"/>
      </linearGradient>
    </defs>
    <polygon points="490,0 880,0 880,31 520,31" fill="url(#tabRed)"/>
  </svg>
  <p class="abs tab-text">CLICK HERE FOR FREE INFO ➜</p>
  <ul class="abs question-list">
    <li>Passionate about Personal Development / Leadership Development?</li>
    <li>Looking to align yourself with an opportunity of substance?</li>
    <li>Ready to be challenged &amp; encouraged to reach new level’s of success?</li>
  </ul>
  <p class="abs develop-band">“LET US SHOW YOU HOW WE’VE TAUGHT OTHERS LIKE YOU<br>TO MAKE A QUANTUM LEAP IN THEIR PERSONAL RESULTS”</p>
  <div class="abs develop-strip">
    <span>- Home Based</span><span>- No cold calling</span><span>- Simple Success Formula</span><span>- Opportunity for “Big Thinker”</span><span>- NOT MLM</span>
  </div>
</section>

<section class="banner banner-tomorrow">
  <svg class="abs tab" viewBox="0 0 880 31" aria-hidden="true">
    <defs>
      <linearGradient id="tabLight" x1="0" y1="0" x2="0" y2="1">
        <stop offset="0" stop-color="#ffffff"/><stop offset="1" stop-color="#d6d6d6"/>
      </linearGradient>
    </defs>
    <polygon points="490,0 880,0 880,31 520,31" fill="url(#tabLight)"/>
  </svg>
  <p class="abs tab-light-text">CLICK HERE FOR FREE INFO ➜</p>
  <h2 class="abs tomorrow-title">CHANGE YOUT TOMORROW - TODAY!</h2>
  <p class="abs tomorrow-lines">Learn to turn your spare time into an EXECUTIVE LEVEL INCOME!<br>In just 2 hours per day you can make a quantum leap in your results</p>
  <p class="abs tomorrow-note">Learn our success formula TODAY so you can enjoy MORE tomorrow!</p>
  <div class="photo photo-couple-casual" role="img" aria-label="Photo of a smiling man and blonde woman posing together at night"></div>
  <div class="abs tomorrow-strip">
    <span>- More Time</span><span>- More Fulfillment</span><span>- More Money</span><span>- More Fun</span>
  </div>
</section>

</body>
</html>
```